Boutique Barre Studio in Geneva

Business card for pilates and dance studio. We are a brand new studio and love our fresh image with our yellow color. This business card is meant for our founder.

```html
<!DOCTYPE html>
<html lang="en">
<head>
<meta charset="utf-8">
<title>Solstice Studio – Founder Business Card</title>
<link rel="stylesheet" href="https://fonts.googleapis.com/css2?family=Arimo:wght@400;700&display=swap">
<style>
  :root {
    --bg-light: #e4e3e0;
    --bg-dark: #b9b7b2;
    --card: #272727;
    --card-deep: #1c1c1c;
    --accent: #f1ea7c;
    --ink-light: #f2f2f2;
  }
  * { box-sizing: border-box; margin: 0; padding: 0; }
  html, body { width: 1200px; height: 801px; overflow: hidden; }
  body {
    background: radial-gradient(ellipse at 30% 10%, var(--bg-light), var(--bg-dark));
    font-family: "Arimo", Arial, sans-serif;
    position: relative;
  }
  .card {
    position: absolute;
    top: 250px;
    width: 520px;
    height: 298px;
    background: var(--card);
    border: 3px solid var(--accent);
    box-shadow: 0 10px 28px rgba(0,0,0,.28);
    overflow: hidden;
  }
  .card--front { left: 60px; }
  .card--back { left: 620px; }

  /* Front */
  .wordmark {
    position: absolute;
    right: 34px;
    top: 30px;
    text-align: right;
    color: var(--accent);
    font-weight: 400;
    line-height: 1;
  }
  .wordmark__name { display: block; font-size: 52px; letter-spacing: -1px; }
  .wordmark__sub { display: block; font-size: 17px; letter-spacing: 4px; margin-top: 4px; }
  .divider {
    position: absolute;
    left: 34px;
    right: 34px;
    top: 150px;
    height: 1px;
    background: var(--accent);
  }
  .founder {
    position: absolute;
    left: 34px;
    bottom: 154px;
  }
  .founder__name {
    color: var(--accent);
    font-weight: 700;
    font-size: 21px;
    letter-spacing: .3px;
  }
  .founder__role { color: var(--ink-light); font-size: 13px; margin-top: 2px; }
  .contacts {
    position: absolute;
    left: 34px;
    top: 168px;
    list-style: none;
    color: var(--ink-light);
    font-size: 12.5px;
  }
  .contacts li { display: flex; align-items: center; gap: 8px; margin-bottom: 6px; }
  .contacts svg { width: 11px; height: 11px; fill: var(--accent); flex: none; }
  .address {
    position: absolute;
    right: 34px;
    top: 168px;
    text-align: right;
    color: var(--ink-light);
    font-size: 12.5px;
    line-height: 1.5;
    font-style: normal;
  }

  /* Back */
  .back-mark {
    position: absolute;
    left: 0; right: 0;
    top: 84px;
    text-align: center;
    color: var(--card-deep);
    font-weight: 400;
    line-height: 1;
  }
  .back-mark__name { display: block; font-size: 76px; letter-spacing: -2px; }
  .back-mark__sub { display: block; font-size: 22px; letter-spacing: 6px; margin-top: 6px; }
</style>
</head>
<body>
  <section class="card card--front" aria-label="Business card front">
    <div class="wordmark">
      <span class="wordmark__name">solstice</span>
      <span class="wordmark__sub">STUDIO</span>
    </div>
    <div class="founder">
      <p class="founder__name">LENA MARCHETTI</p>
      <p class="founder__role">CEO/Founder</p>
    </div>
    <div class="divider"></div>
    <ul class="contacts">
      <li>
        <svg viewBox="0 0 24 24" aria-hidden="true"><path d="M6.6 10.8a15.1 15.1 0 0 0 6.6 6.6l2.2-2.2a1 1 0 0 1 1-.25 11.4 11.4 0 0 0 3.6.57 1 1 0 0 1 1 1V20a1 1 0 0 1-1 1A17 17 0 0 1 3 4a1 1 0 0 1 1-1h3.5a1 1 0 0 1 1 1c0 1.25.2 2.45.57 3.57a1 1 0 0 1-.25 1z"/></svg>
        022-555-0148
      </li>
      <li>
        <svg viewBox="0 0 24 24" aria-hidden="true"><path d="M2 5h20v14H2z M4 7v.5l8 5 8-5V7l-8 5z" fill-rule="evenodd"/></svg>
        hello@solsticestudio.ch
      </li>
      <li>
        <svg viewBox="0 0 24 24" aria-hidden="true"><path d="M12 2a10 10 0 1 0 0 20 10 10 0 0 0 0-20zm0 2c1 0 2.3 2 2.8 5H9.2C9.7 6 11 4 12 4zm-3 7h6a17 17 0 0 1 0 2H9a17 17 0 0 1 0-2zm.2 4h5.6c-.5 3-1.8 5-2.8 5s-2.3-2-2.8-5zM4.3 11h2.7a19 19 0 0 0 0 2H4.3a8 8 0 0 1 0-2zm12.7 0h2.7a8 8 0 0 1 0 2H17a19 19 0 0 0 0-2z"/></svg>
        www.solsticestudio.ch
      </li>
    </ul>
    <address class="address">14 Rue des Vignes<br>Geneva, GE 1204</address>
  </section>

  <section class="card card--back" aria-label="Business card back">
    <div class="back-mark">
      <span class="back-mark__name">solstice</span>
      <span class="back-mark__sub">STUDIO</span>
    </div>
  </section>
</body>
</html>
```